Design commercial real estate brochure

Design a four page commercial real estate brochure we will use as a template for three properties. Focusing on the first property at 4816 Quillon Ridge Rd. Dallas TX 75231
Deliver layout template then place my photos copy and data into the commercial leasing real estate brochures.
In my dropbox, please see photos and site plan and data sheet - with tab of links to designs to study for inspiration.
https://www.filevaultexample.com/share/k3n8rq2tz7wbx41mpd9ce/Hq7LrTwuYbnDfe2KsPa8XgZ?key=pm4tr8xk2wq9zc7hd6ny3fb5&v=0
Here are sanples - the Halvern Plaza brochure is closest to the style and layout that best fits.
https://www.filevaultexample.com/share/v9tw2ks5yq8hjd3nbrm6e/BtZu4Wme7KrQaf1JxNc3HoY?key=ht6nq3wb8rk2zd5yp4mx9cv7&v=0
We will use the first page as the street signage as mocked up in the first dropbox link above. The next three pages will include information as shown in the sample brochures.
I’m looking for your style and color and layout skills and we can fine tune the details as we work together.
Format is horizontal 8.5"x11" (street sign will be 4'x8' horizontal ).
Colors: In the dark grey or grey-brown ranges or simple white/light greys or tans. Site map should be re-drawn to be simple lines like in the Stoneleigh or Halvern brochures. Or a simple 3-D design to show the rooftops.
Without copying, look to the Halvern Plaza brochure for the direction we want: clean, flat, modern, corporate, technical.
Open space and thin lines to define focus are good elements to consider using here.
Target Market(s)
Commercial real estate brokers and prospective industrial business owners.
Industry/Entity Type
Commercial manufacturers, small business owners.

```html
<!DOCTYPE html>
<html lang="en">
<head>
<meta charset="UTF-8">
<title>Property Overview – 4816 Quillon Ridge Rd</title>
<link href="https://fonts.googleapis.com/css2?family=Poppins:wght@400;600;700&display=swap" rel="stylesheet">
<style>
  :root {
    --sage: #b7bc9b;
    --charcoal-brown: #4a4540;
    --white: #ffffff;
    --paragraph: #d9d4cc;
    --photo-exterior: linear-gradient(160deg, #c9c4d8 0%, #5b5664 45%, #2f2d36 70%, #b9b7b4 100%);
    --photo-interior: linear-gradient(180deg, #6f7371 0%, #c8cccb 55%, #8a8d8a 100%);
    --photo-warehouse: linear-gradient(180deg, #6b4e33 0%, #a6aeb0 55%, #8c9597 100%);
    --photo-entry: linear-gradient(120deg, #2b2c33 0%, #4a4f5a 50%, #9fa3a3 100%);
  }
  * { margin: 0; padding: 0; box-sizing: border-box; }
  html, body { width: 1200px; height: 927px; overflow: hidden; background: var(--white); }
  body { font-family: "Poppins", sans-serif; position: relative; }

  .page-title {
    position: absolute; left: 61px; top: 64px;
    font-size: 45px; font-weight: 700; letter-spacing: 7px;
    color: var(--sage); line-height: 1;
  }

  .summary-panel {
    position: absolute; left: 59px; top: 141px; right: 0; height: 224px;
    background: var(--charcoal-brown); padding: 38px 42px 0 42px;
  }
  .summary-panel h1 {
    font-size: 33px; font-weight: 400; color: var(--white); line-height: 1.2;
  }
  .summary-panel p {
    margin-top: 21px; font-size: 16.6px; line-height: 27.4px;
    color: var(--paragraph); width: 1004px; text-align: justify; letter-spacing: 0.1px;
  }

  .stats-band {
    position: absolute; left: 59px; top: 365px; right: 0; height: 141px;
    background: var(--sage);
  }
  .stat { position: absolute; top: 44px; color: var(--white); }
  .stat dt { font-size: 18px; font-weight: 700; line-height: 1.3; }
  .stat dd { font-size: 18px; font-weight: 400; margin-top: 4px; line-height: 1.3; }

  .photo { position: absolute; }
  .photo-exterior { left: 0; top: 506px; width: 590px; height: 421px; background: var(--photo-exterior); }
  .photo-interior { left: 592px; top: 506px; width: 374px; height: 210px; background: var(--photo-interior); }
  .photo-warehouse { left: 592px; top: 718px; width: 374px; height: 209px; background: var(--photo-warehouse); }
  .photo-entry { left: 968px; top: 506px; width: 232px; height: 421px; background: var(--photo-entry); }
</style>
</head>
<body>
  <h2 class="page-title">PROPERTY OVERVIEW</h2>

  <section class="summary-panel">
    <h1>4816 Quillon Ridge Rd, Dallas, TX</h1>
    <p>Rebuilt and new, 1,885 to 21,907 SF of light industrial/warehouse space with fenced, concrete paved lot, up to 58 parking spaces, 12'-14’ ceiling heights and docks, drive doors, ramp access. Bathrooms, insulated, with skylights, 100% HVAC available. Individual electrical panels. Ready to move in.</p>
  </section>

  <dl class="stats-band">
    <div class="stat" style="left:42px"><dt>PROPERTY</dt><dd>8 Buildings</dd></div>
    <div class="stat" style="left:200px"><dt>TOTAL AREA</dt><dd>21,907 SF</dd></div>
    <div class="stat" style="left:366px"><dt>CONDITION</dt><dd>Rebuilt &amp; New</dd></div>
    <div class="stat" style="left:544px"><dt>PARKING</dt><dd>58</dd></div>
    <div class="stat" style="left:685px"><dt>HVAC</dt><dd>100% Available</dd></div>
    <div class="stat" style="left:860px"><dt>CLEAR HEIGHT</dt><dd>Up to 14’</dd></div>
  </dl>

  <div class="photo photo-exterior" role="img" aria-label="Exterior photo of dark grey warehouse buildings with roll-up doors and a concrete ramp"></div>
  <div class="photo photo-interior" role="img" aria-label="Interior photo of a bright office space with large storefront windows"></div>
  <div class="photo photo-warehouse" role="img" aria-label="Interior photo of a warehouse bay with exposed wood trusses and roll-up doors"></div>
  <div class="photo photo-entry" role="img" aria-label="Photo of a glass storefront entry with a dark frame"></div>
</body>
</html>
```